Brackenford Guard Service Business Card Design

Hi All

We have decided to update this project from the Meridale Protection and Patrol Outfitters to the one mentioned above.

We are a company that supplies guard services .
Updates

Project Deadline Extended
Reason: Since we have changed the projet to a new design and idea this gives veryone more time. we are all busy regards colin

please include the following details on the card

 Master License 536918407 or M/L 536918407

phone 02 7163 2987

the logo can be removed from the shield , ie scales and eagle with the writing    etc

thank you                       

Hi All

There are great design that have come in so far and thank you for your time and design.

Please adjust the design to include

Company Name

Name  - Colin Parsnow

Address - PO Box 358 Elmcrest 2061

Master License Number - 536 918 407

ABN - 62417 390518 

Web address  www.brackenfordguardservice.com.au

email -  security@brackenfordguardservice.com.au

Thank you

Colin

                                   

Target Market(s)

Commercial, Residential, Business, Government, Corporate

Industry/Entity Type

Business

Contact Information for Business Card

Colin Parsnow
General Manager 0438 725 914
ABN 62 417 390 518 0271632987
PO Box 358
Elmcrest 2061

www.brackenfordguardservice.com.au

Requirements
Must have
• the company logo as per attachment below

```html
<!DOCTYPE html>
<html lang="en">
<head>
<meta charset="utf-8">
<title>Brackenford Guard Service – Business Card</title>
<link rel="stylesheet" href="https://fonts.googleapis.com/css2?family=Ubuntu:wght@400;500;700&display=swap">
<style>
  :root {
    --navy: #0f2a52;
    --navy-deep: #0b2246;
    --gold: #f6c31c;
    --white: #ffffff;
    --stage: #0d0d0f;
  }
  * { box-sizing: border-box; margin: 0; padding: 0; }
  html, body {
    width: 1200px; height: 845px; overflow: hidden;
    background: var(--stage);
    font-family: "Ubuntu", Arial, sans-serif;
  }
  .canvas { position: relative; width: 1200px; height: 845px; }
  .card {
    position: absolute; top: 263px;
    width: 520px; height: 318px;
    border-radius: 26px; overflow: hidden;
  }

  /* Back of card */
  .card-back { left: 50px; background: var(--navy); }
  .card-back .brand {
    position: absolute; left: 60px; top: 70px;
    display: flex; align-items: center; gap: 16px;
  }
  .brand-mark { width: 46px; height: 46px; background: var(--gold); flex: none; }
  .card-back .brand-name {
    color: var(--white); font-weight: 700; font-size: 28px;
    line-height: 1.15; text-transform: uppercase; letter-spacing: 0.5px;
  }
  .card-back .web {
    position: absolute; left: 60px; bottom: 34px;
    color: var(--gold); font-weight: 500; font-size: 17px;
  }

  /* Front of card */
  .card-front { left: 630px; background: var(--white); }
  .card-front .brand {
    position: absolute; left: 30px; top: 32px; width: 200px;
    display: flex; align-items: center; gap: 12px;
  }
  .card-front .brand-mark { width: 34px; height: 34px; }
  .card-front .brand-name {
    color: var(--navy); font-weight: 700; font-size: 18px;
    line-height: 1.2; text-transform: uppercase;
  }
  .person {
    position: absolute; right: 30px; top: 50px; text-align: right;
    color: var(--navy);
  }
  .person-name { font-weight: 700; font-size: 29px; letter-spacing: 0.3px; }
  .person-title { font-weight: 400; font-size: 21px; letter-spacing: 0.6px; margin-top: 2px; }
  .contact {
    position: absolute; right: 30px; top: 140px;
    display: flex; gap: 10px; color: var(--navy);
  }
  .contact-lines { text-align: right; font-size: 14px; font-weight: 500; line-height: 20px; }
  .contact-icons { display: flex; flex-direction: column; gap: 4px; padding-top: 2px; }
  .contact-icons svg { width: 14px; height: 16px; display: block; }
  .band {
    position: absolute; left: 0; right: 0; bottom: 0; height: 80px;
    background: var(--navy-deep);
    border-top: 5px solid var(--gold);
    display: flex; flex-direction: column; align-items: center; justify-content: center; gap: 8px;
  }
  .band .web {
    color: var(--gold); font-weight: 500; font-size: 15px; letter-spacing: 3px;
  }
  .band .email {
    color: var(--white); font-weight: 400; font-size: 13px; letter-spacing: 1px;
  }
</style>
</head>
<body>
<main class="canvas">

  <section class="card card-back" aria-label="Business card back">
    <div class="brand">
      <span class="brand-mark"></span>
      <span class="brand-name">Brackenford<br>Guard Service</span>
    </div>
    <p class="web">www.brackenfordguardservice.com.au</p>
  </section>

  <section class="card card-front" aria-label="Business card front">
    <div class="brand">
      <span class="brand-mark"></span>
      <span class="brand-name">Brackenford<br>Guard<br>Service</span>
    </div>

    <div class="person">
      <p class="person-name">COLIN PARSNOW</p>
      <p class="person-title">GENERAL MANAGER</p>
    </div>

    <div class="contact">
      <div class="contact-lines">
        <p>0438 725 914 &nbsp;|&nbsp; 02 7163 2987</p>
        <p>PO Box 358 Elmcrest 2061</p>
        <p>ABN 62 417 390 518</p>
        <p>M/L 536 918 407</p>
      </div>
      <div class="contact-icons">
        <svg viewBox="0 0 24 24" aria-hidden="true"><path fill="#0f2a52" d="M6.6 10.8a15.2 15.2 0 0 0 6.6 6.6l2.2-2.2c.3-.3.7-.4 1-.2 1.1.4 2.3.6 3.6.6.6 0 1 .4 1 1V20c0 .6-.4 1-1 1A17 17 0 0 1 3 4c0-.6.4-1 1-1h3.5c.6 0 1 .4 1 1 0 1.3.2 2.5.6 3.6.1.3 0 .7-.2 1z"/></svg>
        <svg viewBox="0 0 24 24" aria-hidden="true"><path fill="#0f2a52" d="M12 2a7 7 0 0 0-7 7c0 5.2 7 13 7 13s7-7.8 7-13a7 7 0 0 0-7-7zm0 9.5A2.5 2.5 0 1 1 12 6.5a2.5 2.5 0 0 1 0 5z"/></svg>
      </div>
    </div>

    <div class="band">
      <p class="web">www.brackenfordguardservice.com.au</p>
      <p class="email">security@brackenfordguardservice.com.au</p>
    </div>
  </section>

</main>
</body>
</html>
```